Multi-Line Insurance PPC Landing Page - Conversion optimized.

We have a PPC landing page used for the general population to get an insurance quote through an agent's site.

We'd like to improve the page for PPC traffic, make it more conversion friendly.

Site should be a single long page.

We will dynamically change the form and headlines on the page depending on what insurance "line" is being called. ie, Lift, Auto, Home, Business.

The enclosed AI file has all of the raw elements we need. We're looking to enhance the design and conversion ability.

Target Market(s)

General public needed insurance services.

Industry/Entity Type

Insurance Broker

Number of Pages Required

1 page

Font styles to use
Sans Serif

Requirements
Must have
• Form, agent picture, name, address.

```html
<!DOCTYPE html>
<html lang="en">
<head>
<meta charset="utf-8">
<title>Insurance Agent – Business Insurance Quote</title>
<link href="https://fonts.googleapis.com/css2?family=Open+Sans:wght@400;600;700&display=swap" rel="stylesheet">
<style>
:root{
  --navy:#1d3f8f;
  --navy-dark:#142d6b;
  --blue:#2a6fd1;
  --green:#2e7d32;
  --ink:#333;
  --muted:#777;
  --line:#d9dde3;
  --panel:#f0f1f3;
  --band:#eceef1;
}
*{box-sizing:border-box;margin:0;padding:0}
html,body{width:841px;height:1200px;overflow:hidden}
body{font-family:"Open Sans",Arial,sans-serif;color:var(--ink);background:#fff;position:relative}
.topbar{height:28px;background:var(--navy);display:flex;align-items:center;justify-content:space-between;padding:0 20px;color:#fff}
.brand{font-weight:700;font-size:15px}
.call{font-size:10px;font-weight:600;display:flex;align-items:center;gap:5px}
.hero{position:relative;height:288px}
.hero-photo{position:absolute;inset:0;background:linear-gradient(180deg,#8aa3b8 0%,#5f7d98 45%,#2b3f57 100%)}
.hero-title{position:absolute;left:24px;top:228px;color:#fff;font-size:22px;font-weight:700;line-height:30px;letter-spacing:.3px}
.cta{position:absolute;right:28px;top:226px;background:var(--blue);color:#fff;font-weight:700;font-size:13px;padding:9px 16px;border-radius:2px}
.lines{position:absolute;left:14px;top:274px;width:746px;height:50px;display:flex;background:#fff;box-shadow:0 2px 4px rgba(0,0,0,.2)}
.line-tab{flex:1;display:flex;align-items:center;gap:6px;padding:0 10px;font-size:9px;font-weight:600;line-height:1.2;border-right:1px solid var(--line)}
.line-tab:last-child{border-right:0}
.line-tab svg{flex:none}
.quote-section{display:flex;gap:16px;padding:54px 78px 0 78px;height:306px}
.agent{width:230px}
.agent-photo{width:150px;height:126px;border:1px solid var(--line);background:linear-gradient(180deg,#d7dde4,#9aa6b4)}
.agent-name{color:var(--navy);font-size:15px;font-weight:700;margin-top:14px}
.agent-phone,.agent-address{font-size:10px;margin-top:6px;line-height:1.5}
.agent-phone{display:flex;align-items:center;gap:5px}
.quote-form{width:440px;height:238px;background:var(--panel);padding:14px 20px}
.form-title{font-size:15px;font-weight:700;color:var(--navy)}
.form-title span{color:var(--ink)}
.fields{display:grid;grid-template-columns:1fr 1fr;column-gap:18px;row-gap:6px;margin-top:10px}
.field label{display:block;font-size:8px;color:var(--muted);margin-bottom:2px}
.input{height:16px;background:#fff;border:1px solid var(--line);font-size:8px;color:#999;padding:2px 4px}
.dob{display:flex;gap:4px}
.dob .input{flex:1}
.submit{display:block;margin:12px auto 0;width:80px;background:var(--green);color:#fff;font-size:9px;font-weight:700;text-align:center;padding:4px 0}
.about{text-align:center;padding:14px 80px 0;height:130px}
h2{font-size:17px;font-weight:600;color:var(--ink)}
h2 b{color:var(--navy);font-weight:700}
.about p{font-size:8.5px;color:var(--muted);line-height:1.6;margin-top:10px}
.reviews{background:var(--band);height:240px;padding-top:12px;text-align:center}
.reviews .sub{font-size:8.5px;color:var(--muted);margin-top:4px}
.review-card{margin:14px auto 0;width:700px;height:140px;background:#fff;display:flex;align-items:center;padding:0 28px;gap:24px;text-align:left}
.review-text{flex:1;font-size:8.5px;color:var(--muted);line-height:1.6}
.review-text .mark{font-size:28px;color:#bbb;line-height:.6;display:block;font-weight:700}
.review-text .by{display:block;text-align:right;color:var(--blue);font-weight:600;margin-top:6px}
.reviewer{width:86px;height:86px;border-radius:50%;border:3px solid #e3e6ea;background:linear-gradient(180deg,#d6dce3,#8d9aab)}
.dots{display:flex;gap:5px;margin:10px 0 0 88px}
.dots i{width:6px;height:6px;border-radius:50%;background:#aab;display:block}
.dots i.on{background:var(--navy)}
.partners{height:96px;display:flex;align-items:center;justify-content:space-between;padding:0 66px}
.partner{font-size:17px;font-weight:700;color:#555}
.arrow{width:16px;height:16px;background:var(--navy);display:flex;align-items:center;justify-content:center}
.footer{position:absolute;left:0;top:1090px;width:841px;height:110px;background:var(--navy);color:#fff}
.disclaimer{text-align:center;padding:10px 60px 0;height:74px}
.disclaimer h3{font-size:10px;font-weight:700}
.disclaimer p{font-size:7px;line-height:1.5;margin-top:4px;opacity:.85}
.footbar{height:36px;background:var(--navy-dark);display:flex;align-items:center;justify-content:space-between;padding:0 20px}
.footbar small{font-size:8px}
.footbar .brand{font-size:14px}
</style>
</head>
<body>
<header class="topbar">
  <div class="brand">Insurance Agent</div>
  <div class="call">
    <svg width="11" height="11" viewBox="0 0 24 24"><path fill="#fff" d="M6.6 10.8a15 15 0 0 0 6.6 6.6l2.2-2.2c.3-.3.7-.4 1-.2 1.1.4 2.3.6 3.6.6.6 0 1 .4 1 1V20c0 .6-.4 1-1 1A17 17 0 0 1 3 4c0-.6.4-1 1-1h3.5c.6 0 1 .4 1 1 0 1.3.2 2.5.6 3.6.1.3 0 .7-.2 1z"/></svg>
    CALL : 123 456 7890
  </div>
</header>

<section class="hero">
  <div class="hero-photo" role="img" aria-label="Business people in suits holding black umbrellas"></div>
  <div class="hero-title">BUSINESS INSURANCE</div>
  <div class="cta">GET A QUOTE!</div>
  <nav class="lines">
    <div class="line-tab"><svg width="34" height="20" viewBox="0 0 34 20"><path fill="#1d3f8f" d="M3 10l4-6h16l6 6h3v6H2v-6z"/><circle cx="9" cy="16" r="3" fill="#fff" stroke="#1d3f8f" stroke-width="2"/><circle cx="25" cy="16" r="3" fill="#fff" stroke="#1d3f8f" stroke-width="2"/></svg>Auto<br>Insurance</div>
    <div class="line-tab"><svg width="24" height="22" viewBox="0 0 24 22"><path fill="#1d3f8f" d="M12 1L1 11h3v10h6v-6h4v6h6V11h3z"/></svg>Home<br>Insurance</div>
    <div class="line-tab"><svg width="24" height="22" viewBox="0 0 24 22"><path fill="#1d3f8f" d="M12 2a10 10 0 0 0-10 10h20A10 10 0 0 0 12 2z"/><path d="M12 12v7a2 2 0 0 1-4 0" stroke="#1d3f8f" stroke-width="2" fill="none"/></svg>Life<br>Insurance</div>
    <div class="line-tab"><svg width="24" height="22" viewBox="0 0 24 22"><path fill="#2a6fd1" d="M12 21L2 11a5.5 5.5 0 0 1 10-6 5.5 5.5 0 0 1 10 6z"/></svg>Health<br>Insurance</div>
    <div class="line-tab"><svg width="24" height="22" viewBox="0 0 24 22"><rect x="2" y="6" width="20" height="14" rx="2" fill="#1d3f8f"/><rect x="8" y="2" width="8" height="5" fill="none" stroke="#1d3f8f" stroke-width="2"/></svg>Business<br>Insurance</div>
    <div class="line-tab"><svg width="24" height="22" viewBox="0 0 24 22"><circle cx="10" cy="3" r="2.5" fill="#1d3f8f"/><path d="M10 6v7h7l3 6M6 10a6 6 0 1 0 8 8" stroke="#1d3f8f" stroke-width="2" fill="none"/></svg>Disability<br>Insurance</div>
  </nav>
</section>

<section class="quote-section">
  <div class="agent">
    <div class="agent-photo" role="img" aria-label="Portrait of the insurance agent"></div>
    <div class="agent-name">Owen Hartley - Agent</div>
    <div class="agent-phone"><svg width="9" height="9" viewBox="0 0 24 24"><path fill="#1d3f8f" d="M6.6 10.8a15 15 0 0 0 6.6 6.6l2.2-2.2c.3-.3.7-.4 1-.2 1.1.4 2.3.6 3.6.6.6 0 1 .4 1 1V20c0 .6-.4 1-1 1A17 17 0 0 1 3 4c0-.6.4-1 1-1h3.5c.6 0 1 .4 1 1 0 1.3.2 2.5.6 3.6.1.3 0 .7-.2 1z"/></svg>(555) 201 4470</div>
    <div class="agent-address">418 Maple Ave.<br>Fresno, CA 93701</div>
  </div>
  <form class="quote-form">
    <div class="form-title">Get An Instant <span>Insurance Quote.</span></div>
    <div class="fields">
      <div class="field"><label>First Name :</label><div class="input"></div></div>
      <div class="field"><label>Height/Weight :</label><div class="input"></div></div>
      <div class="field"><label>Sex :</label><div class="input">Select</div></div>
      <div class="field"><label>Tobacco use :</label><div class="input">Select</div></div>
      <div class="field"><label>Date of Birth :</label><div class="dob"><div class="input">Month</div><div class="input">Day</div><div class="input">Year</div></div></div>
      <div class="field"><label>Phone :</label><div class="input"></div></div>
      <div class="field"><label>Current Health :</label><div class="input">Select</div></div>
      <div class="field"><label>Email :</label><div class="input"></div></div>
    </div>
    <div class="submit">SUBMIT</div>
  </form>
</section>

<section class="about">
  <h2>About <b>Insurance Agent</b></h2>
  <p>Lorem ipsum dolor sit amet, consectetur adipiscing elit, sed diam nonummy nibh euismod tincidunt ut laoreet dolore magna aliquam erat volutpat. Ut wisi enim ad minim veniam, quis nostrud exerci tation ullamcorper suscipit lobortis nisl ut aliquip ex ea commodo consequat. Duis autem vel eum iriure dolor in hendrerit in vulputate velit esse molestie consequat, vel illum dolore eu feugiat nulla facilisis at vero eros et accumsan et iusto odio dignissim qui blandit praesent luptatum zzril delenit augue duis dolore te feugait nulla facilisi.</p>
</section>

<section class="reviews">
  <h2><b>Our</b> Customer Review</h2>
  <div class="sub">Lorem ipsum dolor sit amet, consectetuer adipiscing elit. Donec commodo ligula eget dolor.</div>
  <div class="review-card">
    <div class="review-text">
      <span class="mark">&ldquo;</span>
      Lorem ipsum dolor sit amet, consectetuer adipiscing elit, sed diam nonummy nibh euismod tincidunt ut laoreet dolore magna aliquam erat volutpat. Ut wisi enim ad minim veniam, quis nostrud exerci tation ullamcorper suscipit lobortis nisl ut aliquip ex ea commodo consequat. Duis autem vel eum iriure dolor in hendrerit in vulputate velit esse molestie consequat.
      <span class="by">Lorem ipsum, DOLOR</span>
    </div>
    <div class="reviewer" role="img" aria-label="Photo of the reviewing customer"></div>
  </div>
  <div class="dots"><i></i><i class="on"></i><i></i><i></i></div>
</section>

<section class="partners">
  <div class="arrow"><svg width="8" height="8" viewBox="0 0 8 8"><path d="M6 0L2 4l4 4" stroke="#fff" stroke-width="1.6" fill="none"/></svg></div>
  <div class="partner">Ledgerly</div>
  <div class="partner">Meadowline</div>
  <div class="partner">Corvanta</div>
  <div class="partner">Brightarc</div>
  <div class="partner">Stagewell</div>
  <div class="arrow"><svg width="8" height="8" viewBox="0 0 8 8"><path d="M2 0l4 4-4 4" stroke="#fff" stroke-width="1.6" fill="none"/></svg></div>
</section>

<footer class="footer">
  <div class="disclaimer">
    <h3>Disclaimer</h3>
    <p>Lorem ipsum dolor sit amet, consectetuer adipiscing elit, sed diam nonummy nibh euismod tincidunt ut laoreet dolore magna aliquam erat volutpat. Ut wisi enim ad minim veniam, quis nostrud exerci tation ullamcorper suscipit lobortis nisl ut aliquip ex ea commodo consequat. Duis autem vel eum iriure dolor in hendrerit in vulputate velit esse molestie consequat, vel illum dolore eu feugiat nulla facilisis.</p>
  </div>
  <div class="footbar">
    <small>© 2015 Insurance Agent. All Rights Reserved.</small>
    <div class="brand">Insurance Agent</div>
  </div>
</footer>
</body>
</html>
```